依頼詳細
■コンペで依頼するもの
・トップページ(ワイヤーフレーム参照)
■当選後に依頼するもの
・第2階層ページ(ワイヤーフレーム参照)
・記事ページ(ワイヤーフレーム参照)
・アイキャッチ画像6種類

当選後、追加依頼をプロジェクト形式で発注しますので、受注できる方でお願いします。
追加依頼の予算は4万円以内です。
サイトURL
http://www.morinoyashiro-sample.jp/wp/
ページ数
1ページ
希望イメージ
シンプル 複雑
単色 カラフル
暗い 明るい
日常 高級
遊び心 厳粛
未来的 伝統的
女性的 男性的
希望する色
背景は白指定です。他はお任せします。
納品ファイル
• フォトショップ形式 (.psd)
• PNG形式 (.png)
補足説明
■参考サイト
http://kotobukisha-example.or.jp/jingu/
http://www.hanazakura-example.or.jp/top.php
http://fukuo-mitama.or.jp/

■素材
添付のワイヤーフレームと写真です。
写真は次のアドレスからダウンロードしてください。
http://pelotix.net/morinoyashiro/sozai.zip
現行サイトの画像も利用して頂いて構いません。

※メニュー部の配置は自由にして頂いて構いません。
※ボックス内の文字は画像データとして利用します。他の文字はテキストデータで利用します。
※他有料素材も5千円程度まではお支払できます。

神紋(ロゴマーク)の色は自由に設定して頂いて構いません。
深緑以外であれば問題ないようです。
現行サイトのロゴには「北原郷総鎮守」が含まれています。
ですが、今回はトップページから削除することが決定しています。
説明が不足しておりまして申し訳ございません。
ワイヤーフレーム内、サイトマップのテキストは確定していません。
デザインが分かれば大丈夫です。ダミーのテキストを入れてください。
レスポンシブ対応とありますが、対応は当方で行います。
今回、PC版トップページのイメージアップが最優先ですので、
コンペではレスポンシブを意識せずにデザインして頂いて構いません。
よろしくお願いします。
23日(月) 14:00より選考を開始します。
一時停止の理由:たくさんのご提案を頂きましてありがとうございました。
現在クライアントを含めた席で協議中ですが、どれもクオリティが高く難航しています。
本日中には決定する見込みです。

全体の配色、写真の扱い方を考慮した結果、「クライアントのイメージに近い」という事で選択させて頂きました。

沢山のご提案、誠にありがとうございました。

```html
<!DOCTYPE html>
<html lang="ja">
<head>
<meta charset="utf-8">
<title>森之社 トップページ</title>
<link href="https://fonts.googleapis.com/css2?family=Shippori+Mincho:wght@500;700&family=Noto+Sans+JP:wght@400;700&display=swap" rel="stylesheet">
<style>
:root{
  --nav:#7a2812;
  --nav-dark:#561a0a;
  --ink:#2a2320;
  --muted:#6b625c;
  --line:#d9d2c6;
  --beige:#cdb68c;
  --beige-dark:#a88f62;
  --accent:#b0301a;
  --panel:#1b1715;
  --footer:#3a1e14;
  --paper:#ffffff;
  --soft:#f5f1ea;
}
*{box-sizing:border-box;margin:0;padding:0}
html,body{width:1200px;height:2208px;overflow:hidden;background:var(--paper)}
body{font-family:"Noto Sans JP",sans-serif;color:var(--ink);font-size:13px;line-height:1.6}
.mincho{font-family:"Shippori Mincho",serif}

/* header */
.hero{position:relative;height:368px;overflow:hidden}
.hero-photo-left{position:absolute;left:0;top:0;width:240px;height:368px;background:linear-gradient(160deg,#4c6a3a,#7b3a22 55%,#3c2a1c)}
.hero-photo-right{position:absolute;left:580px;top:0;width:620px;height:368px;background:linear-gradient(170deg,#6d8a5a,#d9d6cf 45%,#8a7a62 80%,#4a3b2a)}
.brand-panel{position:absolute;left:240px;top:0;width:340px;height:368px;background:var(--panel);display:flex;align-items:center;justify-content:center;gap:18px}
.brand-mark{width:64px;height:64px;border-radius:50%;background:#fff}
.brand-name{font-family:"Shippori Mincho",serif;font-weight:700;font-size:64px;color:#fff;letter-spacing:6px}
.hero-tools{position:absolute;right:20px;top:14px;display:flex;gap:6px}
.hero-tools span{background:rgba(255,255,255,.9);font-size:11px;padding:2px 10px;color:var(--ink)}
.hero-caption{position:absolute;left:560px;top:330px;background:rgba(255,255,255,.85);font-size:11px;padding:3px 14px;color:var(--muted)}

.global-nav{height:56px;background:linear-gradient(var(--nav),var(--nav-dark));display:flex;justify-content:center}
.global-nav a{color:#fff;text-decoration:none;font-family:"Shippori Mincho",serif;font-size:16px;font-weight:700;display:flex;align-items:center;padding:0 30px;border-right:1px solid rgba(255,255,255,.3)}
.global-nav a:first-child{border-left:1px solid rgba(255,255,255,.3)}

/* content */
.content{width:960px;margin:24px auto 0;display:flex;gap:24px}
.sidebar{width:240px;flex:none}
.main{width:696px}

.schedule{border:1px solid var(--line)}
.schedule h2{background:var(--panel);color:#fff;font-family:"Shippori Mincho",serif;font-size:17px;padding:10px 14px;display:flex;align-items:center;gap:8px}
.schedule h2::before{content:"";width:12px;height:12px;border-radius:50%;background:var(--accent)}
.schedule ul{list-style:none;padding:8px 16px}
.schedule li{border-bottom:1px dotted var(--line);padding:10px 0;font-size:12px}
.schedule li time{display:block;color:var(--muted);font-size:11px}
.btn{display:inline-block;background:linear-gradient(var(--beige),var(--beige-dark));color:#fff;font-size:12px;padding:5px 18px;border-radius:2px}
.schedule .more{text-align:right;padding:10px 16px 14px}

.banners{margin-top:22px;display:flex;flex-direction:column;gap:8px}
.banner{height:58px;display:flex;align-items:center;padding:0 16px;font-family:"Shippori Mincho",serif;font-weight:700;font-size:15px;color:#fff}
.banner.large{height:82px;background:linear-gradient(90deg,#3d7fb8,#8fc4e4);font-size:17px}
.banner.green{background:linear-gradient(90deg,#4f8a4a,#a4c98a)}
.banner.navy{background:linear-gradient(90deg,#2e4466,#6f86a8)}
.banner.plain{background:var(--soft);color:var(--ink);border:1px solid var(--line)}

.slide{position:relative;height:232px;display:flex;background:var(--soft)}
.slide-text{width:230px;padding:26px 20px;font-size:12px;color:var(--muted)}
.slide-photo{flex:1;background:linear-gradient(170deg,#b9d3e6,#8fb0c4 45%,#7a4d2e 70%,#3e5a74)}

.news{margin-top:26px}
.news h2{font-family:"Shippori Mincho",serif;font-size:20px;color:var(--ink);border-bottom:2px solid var(--nav);padding-bottom:6px;display:flex;align-items:center;gap:8px}
.news h2::before{content:"";width:14px;height:14px;border-radius:50%;background:var(--accent)}
.news ul{list-style:none}
.news li{display:flex;gap:24px;border-bottom:1px dotted var(--line);padding:10px 4px;font-size:13px}
.news li time{color:var(--muted);width:130px}
.news li a{color:var(--accent);text-decoration:none}
.news .more{text-align:right;margin-top:10px}

.guide{margin-top:22px;display:grid;grid-template-columns:1fr 1fr;gap:26px 24px}
.card-photo{position:relative;height:150px}
.card-photo .label{position:absolute;left:0;bottom:12px;background:rgba(27,23,21,.85);color:#fff;font-family:"Shippori Mincho",serif;font-weight:700;font-size:15px;padding:6px 16px}
.card p{font-size:12px;color:var(--muted);margin-top:10px;line-height:1.7}
.card .foot{text-align:right;margin-top:8px}
.p1{background:linear-gradient(160deg,#5c7a4a,#a3402a 55%,#3b2b1e)}
.p2{background:linear-gradient(160deg,#c9c3b6,#f1ede4 50%,#6a5a44)}
.p3{background:linear-gradient(160deg,#3a2a22,#b08a4a 55%,#e6dbc6)}
.p4{background:linear-gradient(160deg,#6f8f5a,#9a4a2a 50%,#4d6a3a)}
.p5{background:linear-gradient(160deg,#d8cdb8,#8a6a44 55%,#3c2e22)}
.p6{background:linear-gradient(160deg,#7a8a6a,#c8b9a0 50%,#4a3a2a)}

.pagetop{width:960px;margin:26px auto 0;text-align:right}
.pagetop span{background:var(--beige);color:#fff;font-size:11px;padding:4px 16px}

.footer{margin-top:14px;border-top:3px solid var(--nav)}
.footer-inner{width:960px;margin:0 auto;height:174px;display:flex;align-items:center;gap:50px}
.footer-brand{width:320px}
.footer-brand .logo{display:flex;align-items:center;gap:12px}
.footer-brand .logo i{width:40px;height:40px;border-radius:50%;background:var(--accent)}
.footer-brand .logo b{font-family:"Shippori Mincho",serif;font-size:34px;color:var(--ink)}
.footer-brand p{font-size:11px;color:var(--muted);margin-top:8px}
.sitemap{flex:1;display:grid;grid-template-columns:repeat(4,1fr);gap:6px 16px;font-size:11px}
.sitemap span::before{content:"▸ ";color:var(--accent)}

.bottom{background:var(--footer);height:186px}
.bottom-inner{width:960px;margin:0 auto;height:100%;display:flex;align-items:center;justify-content:space-between}
.bottom-text{color:#e8ddd0;font-size:11px;line-height:1.9}
.map{width:380px;height:140px;background:linear-gradient(135deg,#dfe6d6,#c8d4bd);position:relative}
.map svg{position:absolute;left:182px;top:46px}
</style>
</head>
<body>
<header class="hero">
  <div class="hero-photo-left" role="img" aria-label="朱塗りの楼門と杜の写真"></div>
  <div class="brand-panel"><span class="brand-mark"></span><span class="brand-name">森之社</span></div>
  <div class="hero-photo-right" role="img" aria-label="白装束の氏子が神輿を担ぐ祭礼の写真"></div>
  <div class="hero-tools"><span>文字サイズ</span><span>大</span><span>小</span></div>
  <div class="hero-caption">北原郷総鎮守 森之社 公式サイト</div>
</header>
<nav class="global-nav">
  <a>森之社について</a><a>祭典・行事</a><a>ご祈祷・その他授与</a><a>境内・周辺案内</a><a>御守・御札</a><a>交　通</a>
</nav>

<div class="content">
  <aside class="sidebar">
    <section class="schedule">
      <h2>行事予定</h2>
      <ul>
        <li><time>平成26年1月1日</time>歳旦祭を斎行します</li>
        <li><time>平成26年1月7日</time>白馬祭を斎行します</li>
        <li><time>平成26年2月3日</time>節分祭を斎行します</li>
        <li><time>平成26年2月11日</time>紀元祭を斎行します</li>
        <li><time>平成26年2月17日</time>祈年祭を斎行します</li>
        <li><time>平成26年3月9日</time>祭頭祭を斎行します</li>
      </ul>
      <div class="more"><span class="btn">一覧を見る</span></div>
    </section>
    <div class="banners">
      <div class="banner large">ご祈祷のご案内</div>
      <div class="banner green">宝物館のご案内</div>
      <div class="banner navy">境内マップ</div>
      <div class="banner plain">崇敬会のご案内</div>
    </div>
  </aside>

  <main class="main">
    <div class="slide">
      <div class="slide-text">平成26年9月1日〜2日<br>例大祭を斎行いたします。<br>多くの皆様のご参拝を心よりお待ち申し上げております。</div>
      <div class="slide-photo" role="img" aria-label="湖上を進む御座船の祭礼写真"></div>
    </div>

    <section class="news">
      <h2>新着情報</h2>
      <ul>
        <li><time>平成26年5月20日</time><a>大祭期間中の駐車場についてのご案内</a></li>
        <li><time>平成26年5月10日</time><a>御田植祭を斎行いたしました</a></li>
        <li><time>平成26年4月28日</time><a>大祭期間中の社務所受付について</a></li>
      </ul>
      <div class="more"><span class="btn">お知らせ一覧</span></div>
    </section>

    <section class="guide">
      <article class="card"><div class="card-photo p1" role="img" aria-label="楼門の写真"><span class="label">森之社について</span></div><p>創建の由来や御祭神、長い歴史と信仰についてご紹介いたします。境内に残る古い社殿もご覧ください。</p><div class="foot"><span class="btn">詳しく見る</span></div></article>
      <article class="card"><div class="card-photo p2" role="img" aria-label="祭典の行列の写真"><span class="label">祭典・行事</span></div><p>年間を通して斎行される祭典や行事をご案内いたします。日程と内容をご確認のうえお参りください。</p><div class="foot"><span class="btn">詳しく見る</span></div></article>
      <article class="card"><div class="card-photo p3" role="img" aria-label="拝殿内の写真"><span class="label">ご祈祷・その他授与</span></div><p>厄除けや安産、家内安全などのご祈祷の受付方法と初穂料についてご案内いたします。</p><div class="foot"><span class="btn">詳しく見る</span></div></article>
      <article class="card"><div class="card-photo p4" role="img" aria-label="参道と社殿の写真"><span class="label">境内・周辺案内</span></div><p>奥宮や御手洗池など境内の見どころと、周辺の散策路についてご紹介いたします。</p><div class="foot"><span class="btn">詳しく見る</span></div></article>
      <article class="card"><div class="card-photo p5" role="img" aria-label="授与所に並ぶ御守の写真"><span class="label">御守・御札</span></div><p>授与所でお受けいただける御守や御札、御朱印の種類についてご案内いたします。</p><div class="foot"><span class="btn">詳しく見る</span></div></article>
      <article class="card"><div class="card-photo p6" role="img" aria-label="鳥居と参道の写真"><span class="label">交　通</span></div><p>電車やお車でお越しの際の交通案内と、駐車場の場所や台数についてご案内いたします。</p><div class="foot"><span class="btn">詳しく見る</span></div></article>
    </section>
  </main>
</div>

<div class="pagetop"><span>▲ ページのトップへ</span></div>

<footer class="footer">
  <div class="footer-inner">
    <div class="footer-brand">
      <div class="logo"><i></i><b>森之社</b></div>
      <p>〒300-0000 北原郡杜町宮中2300番地<br>TEL 0000-00-0000　FAX 0000-00-0000</p>
    </div>
    <div class="sitemap">
      <span>森之社について</span><span>祭典・行事</span><span>ご祈祷のご案内</span><span>境内案内</span>
      <span>御祭神</span><span>年間行事</span><span>授与品</span><span>周辺案内</span>
      <span>由緒・歴史</span><span>例大祭</span><span>御守・御札</span><span>交通案内</span>
      <span>宝物館</span><span>新着情報</span><span>崇敬会</span><span>お問い合わせ</span>
    </div>
  </div>
  <div class="bottom">
    <div class="bottom-inner">
      <p class="bottom-text">【森之社】北原郷総鎮守 森之社 公式サイト<br>ご参拝時間　午前8時30分〜午後4時30分<br>社務所受付　年中無休<br>Copyright © Morinoyashiro. All Rights Reserved.</p>
      <div class="map" role="img" aria-label="周辺地図">
        <svg width="18" height="26" viewBox="0 0 18 26"><path d="M9 0C4 0 0 4 0 9c0 7 9 17 9 17s9-10 9-17C18 4 14 0 9 0z" fill="#b0301a"/><circle cx="9" cy="9" r="3.5" fill="#fff"/></svg>
      </div>
    </div>
  </div>
</footer>
</body>
</html>
```